Looking for amazing PowerPoint Design for sustainable, green last mile delivery company

What we need
- PowerPoint master (16:9)
- Min. 20-30 most used template slides
- Templates for tables, processes, gantt chart, etc.
- Would be good to make it look very modern, green/sustainable, human
- Feel free to extend the color range in addition to the 2 colors from our logo

Who we are
- https://www.brookvane-freight.de/index1.php
- Brookvane Freight is a pioneer in urban green logistics and provides zero-emissions last mile delivery services for its logistics and retail clients
- we take on urban parcel delivery for our clients with a 100% electric commercial vehicles fleet, fair and sustainable working conditions for our employees and a unique professional customer-focused mindset
- We see ourselves as a professional services company who strongly cares about the environment, clients and their customers, and its employees

Attachements
- Company logos - see attached
- Licensed pictures (feel free to use in the designs ) - see here: https://www.filecrate-share.com/sh/72qplmwx39z114b/BBxkTqZr8nVoLpWeHdYUFa3Kcm?dl=0

Requirements
Must have
• We are thinking about at least the following content templates:

- intro/outro (e.g., title, agenda, transition, team, goals, about us, executive summary, key take aways, thank you)
- charts and graphs (e.g., pie, doughnut, bar, line, waterfall, venn)
- image and video (e.g., image only, large image with a sentence)
- text (e.g., text only, text with graph, text with 3/4/5 categories, key numbers)
- process (e.g., steps, phases)
- funnels
- pyramid
- frameworks (with 2/3/4/5 categories)
- timeline (e.g., general/project timeline, gantt)
- services offer
- KPIs/scorecard
- vision, mission, values, culture
- evaluation results
- activities/ToDo page
- policy
- career path
- icons page

Hope this helps. Pls see this as wish list as some of them can also be built by the content from the other slides

```html
<!DOCTYPE html>
<html lang="en">
<head>
<meta charset="utf-8">
<title>Brookvane Freight – Presentation Templates</title>
<link href="https://fonts.googleapis.com/css2?family=Lato:wght@300;400;700&family=Arimo:wght@400&display=swap" rel="stylesheet">
<style>
  :root{
    --canvas:#3a3a3a;
    --paper:#ffffff;
    --ink:#1f1f1f;
    --band-dark:#2b2b2b;
    --band-green:#35c91c;
    --label-green:#8fd43f;
    --brand-green:#45c21a;
    --text-grey:#4a4a4a;
    --g1:#e7f8d6;
    --g2:#d0f3ae;
    --g3:#b2ec7c;
    --g4:#66bd20;
    --g5:#447f14;
  }
  *{box-sizing:border-box;margin:0;padding:0}
  html,body{width:1200px;height:465px;overflow:hidden;background:var(--canvas)}
  .stage{position:absolute;left:0;top:0;width:2576px;height:997px;transform:scale(0.46584);transform-origin:0 0;font-family:"Lato",sans-serif;color:var(--ink)}
  .slide{position:absolute;width:797px;height:448px;background:var(--paper);overflow:hidden}
  .s1{left:46px;top:48px}.s2{left:888px;top:48px}.s3{left:1731px;top:48px}
  .s4{left:46px;top:525px}.s5{left:888px;top:525px}.s6{left:1731px;top:525px}

  .band-green-top{position:absolute;left:0;right:0;top:28px;height:12px;background:var(--band-green)}
  .band-dark-top{position:absolute;left:0;right:0;top:40px;height:45px;background:var(--band-dark)}
  .band-green-bottom{position:absolute;left:0;right:0;bottom:0;height:12px;background:var(--band-green)}

  .corner-mark{position:absolute;right:22px;bottom:30px;display:flex;align-items:center;gap:5px;font-family:"Lato",sans-serif;font-weight:700;font-size:11px;color:var(--brand-green);letter-spacing:.5px}
  .corner-mark .dot{width:14px;height:14px;border-radius:50%;background:var(--brand-green)}

  .kicker{position:absolute;font-size:11px;color:var(--label-green);letter-spacing:.3px}
  .heading{position:absolute;font-weight:400;font-size:28px;letter-spacing:2.5px;color:var(--ink)}
  .body-copy{position:absolute;font-family:"Arimo",sans-serif;font-size:12.6px;line-height:16px;color:var(--ink)}

  /* cover */
  .cover-green{position:absolute;left:0;right:0;top:287px;height:13px;background:var(--band-green)}
  .cover-dark{position:absolute;left:0;right:0;top:300px;height:63px;background:var(--band-dark)}
  .brand-box{position:absolute;left:256px;top:80px;width:286px;height:238px;background:var(--paper);border:1.5px solid var(--band-dark);display:flex;flex-direction:column;align-items:center;justify-content:center;gap:14px}
  .brand-box .mark{width:70px;height:70px;border-radius:50%;background:var(--brand-green)}
  .brand-name{font-weight:700;font-size:26px;color:var(--brand-green);letter-spacing:1px;text-align:center;line-height:28px}
  .brand-name span{display:block;font-size:15px;font-weight:700;letter-spacing:.5px}
  .cover-claim{position:absolute;left:0;right:0;top:327px;text-align:center;color:#fff;font-size:14px;letter-spacing:.3px}

  .photo{position:absolute}
  .photo-van{left:42px;top:14px;width:276px;height:376px;background:linear-gradient(160deg,#f3e8d2 0%,#e4e6e6 35%,#c9ced2 65%,#5f79a8 90%,#9a8676 100%)}

  /* timeline */
  .timeline{position:absolute;left:0;top:0;width:797px;height:448px}
  .stage-note{position:absolute;font-size:11px;line-height:13.5px;color:var(--ink)}
  .stage-note b{display:block;font-weight:400;letter-spacing:.4px}

  /* pie */
  .chart-title{position:absolute;left:560px;top:150px;width:100px;text-align:center;font-family:"Arimo",sans-serif;font-size:13px;color:#444}
  .pie{position:absolute;left:503px;top:180px}
  .legend{position:absolute;left:520px;top:311px;display:flex;gap:12px;font-family:"Arimo",sans-serif;font-size:8px;color:#666}
  .legend i{display:inline-block;width:4px;height:4px;margin-right:3px;vertical-align:middle}

  /* pyramid */
  .pyramid{position:absolute;left:0;top:0}
  .category{position:absolute;left:519px;font-size:11px;line-height:14px}
  .category b{display:block;font-weight:400;letter-spacing:.4px}

  /* services */
  .tile{position:absolute;width:142px;height:143px}
  .tile .caption{position:absolute;left:0;right:0;bottom:0;height:20px;background:var(--band-green);color:#eaffd8;font-size:10.5px;text-align:center;line-height:20px}
  .tile .shot{position:absolute;left:0;right:0;top:0;bottom:20px}
  .services-copy{position:absolute;left:434px;top:240px;width:296px;font-size:12.6px;line-height:16px;color:var(--text-grey)}
</style>
</head>
<body>
<div class="stage">

  <!-- Cover -->
  <section class="slide s1">
    <div class="cover-green"></div>
    <div class="cover-dark"></div>
    <div class="brand-box">
      <div class="mark"></div>
      <div class="brand-name">BROOKVANE FREIGHT<span>SUSTAINABLE LAST MILE</span></div>
    </div>
    <p class="cover-claim">BECAUSE WE CARE ABOUT TREES</p>
  </section>

  <!-- Image with text -->
  <section class="slide s2">
    <div class="band-green-top" style="left:318px"></div>
    <div class="band-dark-top" style="left:318px"></div>
    <div class="photo photo-van" role="img" aria-label="Photo of a white electric delivery van parked on a city street"></div>
    <p class="kicker" style="left:381px;top:141px">TEXT TEXT TEXT</p>
    <h2 class="heading" style="left:380px;top:158px">TITLE</h2>
    <p class="body-copy" style="left:383px;top:214px;width:345px">Lorem ipsum dolor sit amet, consectetur adipiscing elit, sed do eiusmod tempor incididunt ut labore et dolore magna aliqua. Ut enim ad minim veniam, quis nostrud exercitation ullamco laboris nisi ut aliquip ex ea commodo consequat. Duis aute irure dolor in reprehenderit in voluptate velit esse cillum dolore eu fugiat nulla pariatur. Excepteur sint occaecat cupidatat non proident, sunt in culpa qui officia deserunt mollit anim id est laborum.</p>
    <div class="corner-mark"><span class="dot"></span></div>
    <div class="band-green-bottom"></div>
  </section>

  <!-- Timeline -->
  <section class="slide s3">
    <div class="band-green-top"></div>
    <div class="band-dark-top"></div>
    <p class="kicker" style="left:89px;top:139px">TEXT TEXT TEXT</p>
    <h2 class="heading" style="left:88px;top:155px">OUR TIMELINE</h2>
    <svg class="timeline" width="797" height="448" viewBox="0 0 797 448" aria-hidden="true">
      <rect x="131" y="270" width="100" height="17" fill="var(--g1)"/>
      <polygon points="176,287 186,287 181,294" fill="var(--g1)"/>
      <rect x="239" y="270" width="101" height="17" fill="var(--g2)"/>
      <polygon points="284,270 294,270 289,262" fill="var(--g2)"/>
      <rect x="348" y="270" width="101" height="17" fill="var(--g3)"/>
      <polygon points="393,287 403,287 398,295" fill="var(--g3)"/>
      <rect x="457" y="270" width="100" height="17" fill="var(--g4)"/>
      <polygon points="502,270 512,270 507,262" fill="var(--g4)"/>
      <rect x="565" y="270" width="101" height="17" fill="var(--g5)"/>
      <polygon points="610,287 620,287 615,295" fill="var(--g5)"/>
    </svg>
    <p class="stage-note" style="left:255px;top:208px"><b>STAGE</b>Lorem ipsum dolor<br>sit amet</p>
    <p class="stage-note" style="left:472px;top:208px"><b>STAGE</b>Lorem ipsum dolor<br>sit amet</p>
    <p class="stage-note" style="left:147px;top:307px"><b>STAGE</b>Lorem ipsum dolor<br>sit amet</p>
    <p class="stage-note" style="left:364px;top:307px"><b>STAGE</b>Lorem ipsum dolor<br>sit amet</p>
    <p class="stage-note" style="left:581px;top:307px"><b>STAGE</b>Lorem ipsum dolor<br>sit amet</p>
    <div class="corner-mark"><span class="dot"></span></div>
    <div class="band-green-bottom"></div>
  </section>

  <!-- Text with chart -->
  <section class="slide s4">
    <div class="band-green-top"></div>
    <div class="band-dark-top"></div>
    <p class="kicker" style="left:108px;top:140px">TEXT TEXT TEXT</p>
    <h2 class="heading" style="left:107px;top:157px">TITLE</h2>
    <p class="body-copy" style="left:110px;top:213px;width:345px">Lorem ipsum dolor sit amet, consectetur adipiscing elit, sed do eiusmod tempor incididunt ut labore et dolore magna aliqua. Ut enim ad minim veniam, quis nostrud exercitation ullamco laboris nisi ut aliquip ex ea commodo consequat. Duis aute irure dolor in reprehenderit in voluptate velit esse cillum dolore eu fugiat nulla pariatur. Excepteur sint occaecat cupidatat non proident, sunt in culpa qui officia deserunt mollit anim id est laborum.</p>
    <p class="chart-title">Impact</p>
    <svg class="pie" width="220" height="125" viewBox="0 0 220 125" aria-label="Pie chart: Impact by quarter">
      <path d="M7 50 L7 74 A103 45 0 0 0 213 74 L213 50 A103 45 0 0 1 7 50 Z" fill="#3f8d0c"/>
      <path d="M7 50 L7 74 A103 45 0 0 0 49.4 110.4 L49.4 86.4 A103 45 0 0 1 7 50 Z" fill="#59ad14"/>
      <path d="M110 50 L110 5 A103 45 0 1 1 49.4 86.4 Z" fill="#5fae16"/>
      <path d="M110 50 L49.4 86.4 A103 45 0 0 1 12 36.1 Z" fill="#7fd524"/>
      <path d="M110 50 L12 36.1 A103 45 0 0 1 49.4 13.6 Z" fill="#a4e85a"/>
      <path d="M110 50 L49.4 13.6 A103 45 0 0 1 110 5 Z" fill="#cdf2a6"/>
    </svg>
    <div class="legend">
      <span><i style="background:#5fae16"></i>1st Qtr</span>
      <span><i style="background:#7fd524"></i>2nd Qtr</span>
      <span><i style="background:#a4e85a"></i>3rd Qtr</span>
      <span><i style="background:#cdf2a6"></i>4th Qtr</span>
    </div>
    <div class="corner-mark"><span class="dot"></span></div>
    <div class="band-green-bottom"></div>
  </section>

  <!-- Pyramid -->
  <section class="slide s5">
    <div class="band-green-top"></div>
    <div class="band-dark-top"></div>
    <h2 class="heading" style="left:70px;top:130px">TITLE</h2>
    <svg class="pyramid" width="797" height="448" viewBox="0 0 797 448" aria-hidden="true">
      <defs>
        <marker id="tip" viewBox="0 0 6 6" refX="5" refY="3" markerWidth="5" markerHeight="5" orient="auto-start-reverse"><path d="M0 0 L6 3 L0 6 Z" fill="context-stroke"/></marker>
      </defs>
      <polygon points="269,118 298,167 240,167" fill="var(--g1)"/>
      <polygon points="234,177 304,177 334,227 204,227" fill="var(--g2)"/>
      <polygon points="198,237 340,237 370,287 168,287" fill="var(--g3)"/>
      <polygon points="162,297 376,297 406,347 132,347" fill="var(--g4)"/>
      <polygon points="126,357 412,357 442,407 96,407" fill="var(--g5)"/>
      <line x1="312" y1="142" x2="497" y2="142" stroke="var(--g1)" stroke-width="2" marker-start="url(#tip)" marker-end="url(#tip)"/>
      <line x1="345" y1="202" x2="497" y2="202" stroke="var(--g2)" stroke-width="2" marker-start="url(#tip)" marker-end="url(#tip)"/>
      <line x1="382" y1="261" x2="497" y2="261" stroke="var(--g3)" stroke-width="2" marker-start="url(#tip)" marker-end="url(#tip)"/>
      <line x1="409" y1="318" x2="497" y2="318" stroke="var(--g4)" stroke-width="2" marker-start="url(#tip)" marker-end="url(#tip)"/>
      <line x1="445" y1="377" x2="497" y2="377" stroke="var(--g5)" stroke-width="2" marker-start="url(#tip)" marker-end="url(#tip)"/>
    </svg>
    <p class="category" style="top:130px"><b>CATEGORY</b>Lorem ipsum dolor sit amet</p>
    <p class="category" style="top:189px"><b>CATEGORY</b>Lorem ipsum dolor sit amet</p>
    <p class="category" style="top:249px"><b>CATEGORY</b>Lorem ipsum dolor sit amet</p>
    <p class="category" style="top:305px"><b>CATEGORY</b>Lorem ipsum dolor sit amet</p>
    <p class="category" style="top:364px"><b>CATEGORY</b>Lorem ipsum dolor sit amet</p>
    <div class="corner-mark"><span class="dot"></span></div>
    <div class="band-green-bottom"></div>
  </section>

  <!-- Services -->
  <section class="slide s6">
    <div class="band-green-top"></div>
    <div class="band-dark-top"></div>
    <div class="tile" style="left:82px;top:107px">
      <div class="shot" role="img" aria-label="Photo of a business handshake in an office" style="background:linear-gradient(135deg,#c9d3dc,#5a7190)"></div>
      <div class="caption">Professional All Around</div>
    </div>
    <div class="tile" style="left:248px;top:107px">
      <div class="shot" role="img" aria-label="Photo of a green electric van driving on a road" style="background:linear-gradient(160deg,#9fb0a8,#5fbd2a 60%,#45533f)"></div>
      <div class="caption">Zero-Emission Delivery</div>
    </div>
    <div class="tile" style="left:82px;top:270px">
      <div class="shot" role="img" aria-label="Photo of a delivery driver carrying a parcel in front of a van" style="background:linear-gradient(160deg,#b9c0c6,#3c5478 60%,#c9a06a)"></div>
      <div class="caption">Highly Trained Drivers</div>
    </div>
    <div class="tile" style="left:248px;top:270px">
      <div class="shot" role="img" aria-label="Photo of a parcel being handed to a customer at her door" style="background:linear-gradient(160deg,#dfe3e6,#7c8d9e 55%,#2f4a6e)"></div>
      <div class="caption">Rare Customer Focus</div>
    </div>
    <p class="kicker" style="left:434px;top:165px">WHAT WE OFFER</p>
    <h2 class="heading" style="left:433px;top:181px">OUR SERVICES</h2>
    <p class="services-copy">Brookvane Freight provides last mile delivery services in urban areas to clients in the logistics and retail space. Our permanent employees are all highly trained and commit to highest professional standards which we continuously review and further develop with them.</p>
    <div class="corner-mark"><span class="dot"></span></div>
    <div class="band-green-bottom"></div>
  </section>

</div>
</body>
</html>
```